Larkfield Clinic Booklet 2016

Larkfield Clinic is a multi-specialty Practice in Midtown Manhattan offering advanced care in multiple areas of medicine. See our table of contents (PDF Uploaded)
Our designed booklet should be clean, easy to read, contemporary, high-end and elegant.
We need a general theme, Layout for cover and templates for internal.
We are entertaining the idea of two different sizes
8 x 10
or
11 x 8.5
Our tagline " The Future of Medicine is Here"
We will provide all the text content
The link to our website
www.LarkfieldCL.example
Uploaded files are as follows.. Logo, Our Team Photo and the PDF listing the table of contents.

```html
<!DOCTYPE html>
<html lang="en">
<head>
<meta charset="utf-8">
<title>Larkfield Clinic Booklet Cover</title>
<link rel="stylesheet" href="https://fonts.googleapis.com/css2?family=Montserrat:wght@400;500&display=swap">
<style>
  :root {
    --stage: #e9edf2;
    --cover-blue: #1f6fd1;
    --block-blue: #1b63c8;
    --block-light: #2a7ad8;
    --deep-blue: #1553ae;
    --accent-yellow: #f7bd22;
    --accent-gold: #eaa910;
    --shadow-navy: #101c33;
    --photo-cream: #efe6d4;
    --photo-wall: #d9cdb8;
    --photo-scrubs: #8fb0e0;
    --photo-deep: #4d6a98;
    --white: #ffffff;
  }
  html, body {
    margin: 0;
    padding: 0;
    width: 1200px;
    height: 701px;
    overflow: hidden;
    background: var(--stage);
  }
  .booklet-cover {
    position: absolute;
    left: 186px;
    top: 30px;
    width: 828px;
    height: 640px;
    box-shadow: 0 12px 34px rgba(13, 31, 61, 0.28);
  }
  .booklet-cover svg { display: block; }
  .brand-name {
    font-family: "Montserrat", sans-serif;
    font-weight: 500;
    fill: var(--white);
    letter-spacing: 1.5px;
  }
  .tagline {
    font-family: "Montserrat", sans-serif;
    font-weight: 400;
    fill: var(--white);
    letter-spacing: 0.6px;
  }
</style>
</head>
<body>
  <div class="booklet-cover">
    <svg width="828" height="640" viewBox="0 0 828 640" xmlns="http://www.w3.org/2000/svg">
      <defs>
        <linearGradient id="team-photo-tone" x1="0" y1="0" x2="0.35" y2="1">
          <stop offset="0" stop-color="var(--photo-cream)"/>
          <stop offset="0.3" stop-color="var(--photo-wall)"/>
          <stop offset="0.55" stop-color="var(--photo-scrubs)"/>
          <stop offset="0.85" stop-color="var(--photo-deep)"/>
          <stop offset="1" stop-color="var(--shadow-navy)"/>
        </linearGradient>
        <linearGradient id="band-tone" x1="0" y1="0" x2="0" y2="1">
          <stop offset="0" stop-color="var(--accent-yellow)"/>
          <stop offset="1" stop-color="var(--accent-gold)"/>
        </linearGradient>
      </defs>

      <!-- team photo area -->
      <rect class="team-photo" role="img" aria-label="Team photo of the clinic's doctors and nurses in scrubs and white coats"
            width="828" height="640" fill="url(#team-photo-tone)"/>

      <!-- stepped header blocks -->
      <g class="header-blocks">
        <rect x="0" y="0" width="828" height="70" fill="var(--deep-blue)"/>
        <rect x="0" y="0" width="140" height="330" fill="var(--block-blue)"/>
        <rect x="140" y="0" width="90" height="300" fill="var(--deep-blue)"/>
        <rect x="230" y="0" width="230" height="270" fill="var(--block-light)"/>
        <rect x="460" y="0" width="160" height="180" fill="var(--block-blue)"/>
        <rect x="620" y="0" width="208" height="110" fill="var(--deep-blue)"/>
      </g>

      <!-- yellow step edges -->
      <g class="step-edges" fill="url(#band-tone)">
        <rect x="0" y="330" width="150" height="14"/>
        <rect x="140" y="300" width="100" height="14"/>
        <rect x="230" y="270" width="240" height="14"/>
        <rect x="460" y="180" width="170" height="14"/>
        <rect x="620" y="110" width="208" height="14"/>
      </g>

      <!-- lower accent bands -->
      <g class="lower-bands">
        <path d="M828 380 V640 H0 V600 H380 V540 H560 V470 H700 V400 Z" fill="var(--shadow-navy)"/>
        <g fill="url(#band-tone)">
          <rect x="0" y="586" width="390" height="22"/>
          <rect x="380" y="526" width="190" height="22"/>
          <rect x="560" y="456" width="150" height="22"/>
          <rect x="700" y="386" width="128" height="22"/>
        </g>
      </g>

      <!-- brand lockup -->
      <g class="brand-lockup">
        <circle cx="345" cy="88" r="26" fill="var(--deep-blue)" stroke="var(--white)" stroke-width="2"/>
        <text class="brand-name" x="345" y="150" text-anchor="middle" font-size="22">LARKFIELD</text>
        <text class="brand-name" x="345" y="177" text-anchor="middle" font-size="22">CLINIC</text>
        <text class="tagline" x="345" y="208" text-anchor="middle" font-size="12">The Future of Medicine is Here</text>
      </g>
    </svg>
  </div>
</body>
</html>
```